make it look old timey and motherly but mordern...bath soak with cooling vapors. tall pine hush

need a bath soak label...cooling vapors. will be in a pouch like below. dont pay attention to the design, just attatching so you know the kind of pouch itll be in. need something trusty, minimal and clean...its called tall pine hush bath soak the best bath yull ever take.... for sore muscles, cooling vapors, smells good...made with menthol lemon and eucalyptus...give me something good.

Target Market(s)

make it look old timey and motherly but mordern

Font styles to use
Serif
Sans Serif

Colors
0054AA
0677BA
7BADD7
CADEEF
E8F1F8
0094D4
00A9DD
6FCCEA
C7EBF8
E9F6FB
FFF300
FFF600
FEFA6F
FFFEC7
FFFEE8
FFC000
F8CF3A
FAE287
FDF2CF
FEFAEE
E54698
E96AAD
F1A4CE
F9D9EA
FCEFF6
6B429C
8869AF
B7A5CE
E3DAEB
F3F0F8

```html
<!DOCTYPE html>
<html lang="en">
<head>
<meta charset="utf-8">
<title>Tall Pine Hush Bath Soak Label</title>
<link rel="stylesheet" href="https://fonts.googleapis.com/css2?family=Open+Sans:wght@600;800&family=Playfair+Display:ital,wght@0,800;1,500&display=swap">
<style>
  :root {
    --page-bg: #efefef;
    --marble-white: #f3f5f3;
    --marble-lilac: #e4c6ee;
    --ink: #2e2e2e;
    --ink-soft: #4a4a4a;
    --rule: #6b429c;
  }
  html, body {
    margin: 0;
    padding: 0;
    width: 1200px;
    height: 800px;
    overflow: hidden;
    background: var(--page-bg);
  }
  .canvas {
    position: relative;
    width: 1200px;
    height: 800px;
  }
  .label {
    position: absolute;
    left: 350px;
    top: 25px;
    width: 500px;
    height: 750px;
    overflow: hidden;
  }
  .label__marble {
    position: absolute;
    inset: 0;
    background:
      radial-gradient(ellipse 60% 18% at 65% 12%, var(--marble-lilac), transparent 70%),
      radial-gradient(ellipse 40% 14% at 15% 55%, var(--marble-lilac), transparent 70%),
      radial-gradient(ellipse 50% 16% at 75% 90%, var(--marble-lilac), transparent 70%),
      linear-gradient(165deg, var(--marble-white) 0%, #eedcf3 35%, var(--marble-white) 60%, #ead4f1 100%);
  }
  .label__text {
    position: absolute;
    left: 30px;
    right: 30px;
    top: 280px;
    text-align: center;
    color: var(--ink);
  }
  .label__brand {
    margin: 0;
    font-family: "Open Sans", Arial, sans-serif;
    font-weight: 800;
    font-size: 30px;
    line-height: 1;
    letter-spacing: 2px;
  }
  .label__product {
    margin: 8px 0 0;
    font-family: "Playfair Display", Georgia, serif;
    font-weight: 800;
    font-size: 74px;
    line-height: 1;
  }
  .label__tagline {
    margin: 12px 0 0;
    font-family: "Playfair Display", Georgia, serif;
    font-style: italic;
    font-weight: 500;
    font-size: 22px;
    line-height: 1.1;
    color: var(--ink-soft);
  }
  .label__rule {
    width: 120px;
    height: 2px;
    margin: 18px auto 14px;
    background: var(--rule);
  }
  .label__benefit,
  .label__ingredients {
    margin: 0;
    font-family: "Open Sans", Arial, sans-serif;
    font-weight: 600;
    font-size: 13px;
    line-height: 1.6;
    letter-spacing: 2px;
    color: var(--ink);
  }
</style>
</head>
<body>
  <main class="canvas">
    <section class="label">
      <div class="label__marble" role="img" aria-label="White marble texture with lilac and violet veins"></div>
      <div class="label__text">
        <p class="label__brand">TALL PINE HUSH</p>
        <h1 class="label__product">BATH SOAK</h1>
        <p class="label__tagline">the best bath you'll ever take</p>
        <div class="label__rule"></div>
        <p class="label__benefit">COOLING VAPORS FOR SORE MUSCLES</p>
        <p class="label__ingredients">MENTHOL · LEMON · EUCALYPTUS</p>
      </div>
    </section>
  </main>
</body>
</html>
```